Milo's RV Park & Lodge Business Card

business card

Target Market(s)

RVers, Campers, Outdoor people, hunters, fishermen

Contact Information for Business Card

I would like a business card with a picture of my RV Park on one side and the following information on the other side:

Milo Hartvick
Milo's RV Park & Lodge
317 4th St NW
Alder Bay MN 56901
701-582-9017 (call)
701-624-7150 (call or text)
www.milosbrookfieldrvpark.example
milosbrookfield@mailbox.example

The color scheme is white with black and red

Colors
ec1f27
ffffff

Requirements
Must have
• picture of my rv park on one side

```html
<!DOCTYPE html>
<html lang="en">
<head>
<meta charset="utf-8">
<title>Milo's RV Park &amp; Lodge – Business Card</title>
<link href="https://fonts.googleapis.com/css2?family=Noto+Sans:ital,wght@0,400;0,700;1,400&display=swap" rel="stylesheet">
<style>
  :root {
    --page-bg: #1f1d1c;
    --card-bg: #3a3735;
    --brand-red: #ec1f27;
    --text-white: #ffffff;
    --sky: #cfdcea;
    --trees: #4f6f3c;
    --gravel: #b8a78a;
    --grass: #5c8c3c;
  }
  * { margin: 0; padding: 0; box-sizing: border-box; }
  html, body {
    width: 1200px; height: 1200px; overflow: hidden;
    background: var(--page-bg);
    font-family: "Noto Sans", "Verdana", sans-serif;
    color: var(--text-white);
  }
  .card {
    position: absolute; left: 150px;
    width: 900px; height: 520px;
    background: var(--card-bg);
    box-shadow: 0 10px 30px rgba(0,0,0,.5);
    overflow: hidden;
  }
  .card--back { top: 60px; }
  .card--front { top: 620px; }

  .brand { position: absolute; }
  .brand__name {
    display: flex; align-items: center; gap: 14px;
    font-weight: 700; white-space: nowrap;
  }
  .brand__mark { background: var(--brand-red); flex: none; }
  .brand__tagline { font-style: italic; white-space: nowrap; }

  .card--back .brand { left: 46px; top: 120px; }
  .card--back .brand__name { font-size: 50px; }
  .card--back .brand__mark { width: 30px; height: 30px; }
  .card--back .brand__tagline { font-size: 16px; margin: 2px 0 0 30px; }

  .holder {
    position: absolute; left: 46px; top: 292px;
    font-size: 24px; font-weight: 700;
  }
  .contact-list, .address {
    position: absolute; bottom: 30px;
    font-size: 21px; line-height: 25px; list-style: none;
  }
  .contact-list { left: 46px; }
  .address { right: 44px; text-align: right; font-style: normal; }

  .park-photo { position: absolute; inset: 0; width: 900px; height: 520px; }
  .card--front .brand { right: 62px; top: 150px; text-align: center; }
  .card--front .brand__name { font-size: 40px; gap: 10px; }
  .card--front .brand__mark { width: 24px; height: 24px; }
  .card--front .brand__tagline { font-size: 13px; margin-top: 2px; }
</style>
</head>
<body>

<section class="card card--back">
  <div class="brand">
    <div class="brand__name"><span class="brand__mark"></span>Milo's RV Park</div>
    <p class="brand__tagline">parked right in the heart of all the fun!!!</p>
  </div>
  <p class="holder">Milo Hartvick</p>
  <ul class="contact-list">
    <li>701-582-9017 (call)</li>
    <li>701-624-7150 (call or text)</li>
    <li>www.milosbrookfieldrvpark.example</li>
    <li>milosbrookfield@mailbox.example</li>
  </ul>
  <address class="address">
    Milo's RV Park &amp; Lodge<br>
    317 4th St NW<br>
    Alder Bay MN 56901
  </address>
</section>

<section class="card card--front">
  <svg class="park-photo" viewBox="0 0 900 520" role="img" aria-label="Photo of the RV park: motorhomes and trailers parked along a gravel lot with trees and grass under a pale sky">
    <defs>
      <linearGradient id="park-tones" x1="0" y1="0" x2="0" y2="1">
        <stop offset="0.15" stop-color="var(--sky)"/>
        <stop offset="0.5" stop-color="#dfe7ee"/>
        <stop offset="0.6" stop-color="var(--trees)"/>
        <stop offset="0.72" stop-color="#e4e1d8"/>
        <stop offset="0.84" stop-color="var(--gravel)"/>
        <stop offset="0.93" stop-color="var(--grass)"/>
      </linearGradient>
    </defs>
    <path d="M0,93 C250,78 390,110 480,200 C570,285 700,300 900,280 L900,520 L0,520 Z" fill="url(#park-tones)"/>
  </svg>
  <div class="brand">
    <div class="brand__name"><span class="brand__mark"></span>Milo's RV Park</div>
    <p class="brand__tagline">parked right in the heart of all the fun!!!</p>
  </div>
</section>

</body>
</html>
```